Boutique Barre Studio in Geneva

Business card for pilates and dance studio. We are a brand new studio and love our fresh image with our yellow color. This business card is meant for our founder.

```html
<!DOCTYPE html>
<html lang="en">
<head>
<meta charset="utf-8">
<title>Poise Studio – Business Card</title>
<link rel="stylesheet" href="https://fonts.googleapis.com/css2?family=Montserrat:wght@300;400;700&display=swap">
<style>
  :root {
    --backdrop: #b4b4b4;
    --card-black: #050505;
    --ink-white: #ffffff;
    --ink-dark: #1c1714;
    --tan-deep: #b8906a;
    --tan-mid: #d2ae8e;
    --tan-light: #ecd6c0;
    --rule: #8a8a8a;
  }
  * { margin: 0; padding: 0; box-sizing: border-box; }
  html, body {
    width: 1200px; height: 846px; overflow: hidden;
    background: var(--backdrop);
    font-family: "Montserrat", sans-serif;
  }
  .sheet {
    width: 1200px; height: 846px;
    display: flex; align-items: center; justify-content: center; gap: 40px;
  }
  .card {
    position: relative;
    width: 540px; height: 309px;
    border-radius: 26px;
    overflow: hidden;
  }
  /* Front side */
  .card-front { background: var(--card-black); color: var(--ink-white); }
  .brand {
    position: absolute; left: 0; right: 0; top: 48px;
    text-align: center;
    font-weight: 400; font-size: 46px; letter-spacing: 2px; line-height: 1;
  }
  .brand-dark { color: var(--ink-dark); }
  .founder {
    position: absolute; left: 50px; top: 170px;
  }
  .founder-name { font-weight: 700; font-size: 15px; }
  .founder-role { font-weight: 300; font-size: 14px; margin-top: 4px; }
  .contact {
    position: absolute; left: 285px; top: 152px;
    list-style: none; font-weight: 300; font-size: 14px;
  }
  .contact li { display: flex; align-items: center; gap: 9px; margin-bottom: 8px; }
  .contact svg { width: 17px; height: 17px; flex: none; }
  .divider {
    position: absolute; left: 50px; right: 50px; top: 228px;
    border-top: 1px solid var(--rule);
  }
  .address {
    position: absolute; left: 0; right: 0; top: 244px;
    text-align: center; font-weight: 300; font-size: 13.5px; letter-spacing: 0.3px;
  }
  /* Back side */
  .card-back { color: var(--ink-dark); }
  .photo-field {
    position: absolute; inset: 0;
    background:
      radial-gradient(ellipse at 72% 40%, var(--tan-deep) 0%, transparent 55%),
      linear-gradient(160deg, var(--tan-deep) 0%, var(--tan-mid) 55%, var(--tan-light) 100%);
  }
  .card-back .brand { top: 120px; left: 40px; right: auto; text-align: left; }
  .web {
    position: absolute; left: 150px; bottom: 30px;
    font-weight: 400; font-size: 14px; letter-spacing: 0.5px;
  }
</style>
</head>
<body>
<main class="sheet">
  <section class="card card-front">
    <div class="brand">poise studio</div>
    <div class="founder">
      <p class="founder-name">Mira Valcourt</p>
      <p class="founder-role">Founder</p>
    </div>
    <ul class="contact">
      <li>
        <svg viewBox="0 0 24 24" fill="none" stroke="currentColor" stroke-width="1.8" stroke-linejoin="round"><path d="M5 3h4l2 5-2.5 1.5a11 11 0 0 0 6 6L16 13l5 2v4a2 2 0 0 1-2 2A16 16 0 0 1 3 5a2 2 0 0 1 2-2z"/></svg>
        +33 745210387
      </li>
      <li>
        <svg viewBox="0 0 24 24" fill="none" stroke="currentColor" stroke-width="1.8" stroke-linejoin="round"><rect x="3" y="5" width="18" height="14" rx="1.5"/><path d="M3 6l9 7 9-7"/></svg>
        hello@poise-studio.com
      </li>
    </ul>
    <div class="divider"></div>
    <p class="address">Rue des Lilas 12 / 1205 Geneva / Switzerland</p>
  </section>

  <section class="card card-back">
    <div class="photo-field" role="img" aria-label="Photograph of a dancer leaping against a warm beige studio backdrop"></div>
    <div class="brand brand-dark">poise studio</div>
    <p class="web">WWW.POISE-STUDIO.COM</p>
  </section>
</main>
</body>
</html>
```